Independent Artist - Album Cover Design

I need a full album cover design for my debut album Velvet After Dark. The album is a love-inspired, passionate, soulful, relationship laden album. An album that can relate to anyone in love (or lust/obsession), going through ups and downs of relationships,and overcoming any hardships and enjoying the joys of true love, sex, and companionship. My first thoughts are a black and white design with the color red poppin off in there maybe in some of the lettering but I am open to some creative ideas. Looking for something clean and sexy that represents what the album is about. I was thinking maybe having a photo of myself on there but don't really have any that would work Stay Late but I can take some and send a link if you have some good ideas.

My Artist name if I didnt mention before is Velmora. I would like that on the album cover as well. Also I need a full album cover Front and Back. Below is the track list if you could incorporate that as well. And below is also a link to some photos. Thank you.

https://www.filecrate-demo.net/sh/qk4rmvplwex7dan/TyuNpoeRkW

1 .Silk Skin (Feat. Marlon Quickstep)
2.  Midnight Heat (Feat. Dolo Vey)
3 .Feel The Wave (Feat. Tumo)
4 . Hold Me Closer
5. Sidewayz
6.  For Us (Feat. Dolo Vey)
7 .She Fits Right In Here
8 . Stay Late
9 . Weekend Is Ours
10.  Down This Hall
11.  We Might
12 . Seasons Of Desire

New Clearer Pictures Posted to filecrate folder. Thanks.

https://www.filecrate-demo.net/sh/qk4rmvplwex7dan/KKRm5t71hZyWqNofBxeLuvcsn

```html
<!DOCTYPE html>
<html lang="en">
<head>
<meta charset="utf-8">
<title>Velmora – Velvet After Dark – Back Tray</title>
<link rel="stylesheet" href="https://fonts.googleapis.com/css2?family=Anton&family=Gochi+Hand&family=Permanent+Marker&display=swap">
<style>
  :root {
    --page: #ffffff;
    --spine: #c9c9c9;
    --panel: #c3c3c3;
    --wall: #d3d3d3;
    --ink: #111111;
    --accent: #d10f0f;
    --stamp: #858585;
  }
  html, body { margin: 0; padding: 0; overflow: hidden; }
  body { width: 1200px; height: 1000px; background: var(--page); position: relative; }

  .tray { position: absolute; left: 165px; top: 150px; width: 872px; height: 688px; }

  .spine {
    position: absolute; top: 0; width: 33px; height: 688px; background: var(--spine);
    display: flex; flex-direction: column; align-items: center; justify-content: space-between;
    padding: 74px 0 76px; box-sizing: border-box;
  }
  .spine--left { left: 0; }
  .spine--right { left: 838px; }
  .spine__artist {
    writing-mode: vertical-rl; font-family: "Anton", sans-serif; font-size: 21px;
    letter-spacing: 1px; color: var(--ink); line-height: 1;
  }
  .spine__title {
    writing-mode: vertical-rl; font-family: "Gochi Hand", cursive; font-size: 25px;
    color: var(--accent); line-height: 1;
  }

  .panel { position: absolute; left: 37px; top: 0; width: 798px; height: 688px; background: var(--panel); }
  .panel__wall { position: absolute; left: 0; top: 0; width: 243px; height: 688px; background: linear-gradient(90deg, #d8d8d8, var(--wall) 70%, #cdcdcd); }

  .album-title {
    position: absolute; left: 88px; top: 52px; margin: 0;
    font-family: "Permanent Marker", cursive; font-weight: 400; font-size: 32px;
    line-height: 30px; color: var(--accent); transform: rotate(4deg);
  }
  .album-title span { display: block; }
  .album-title span:nth-child(2) { padding-left: 22px; }
  .album-title span:nth-child(3) { padding-left: 18px; }

  .artist-stamp {
    position: absolute; left: 70px; top: 150px; height: 505px; width: 140px;
    writing-mode: vertical-rl; transform: rotate(180deg);
    font-family: "Anton", sans-serif; font-size: 134px; line-height: 140px;
    color: var(--stamp); text-align: center; letter-spacing: 2px;
  }

  .tracklist { list-style: none; margin: 0; padding: 0; }
  .track {
    position: absolute; white-space: nowrap; font-family: "Gochi Hand", cursive;
    font-size: 31px; line-height: 36px; color: var(--ink); word-spacing: 6px;
  }
  .track__feat { font-size: 20px; word-spacing: 2px; margin-left: 6px; }

  .credits {
    position: absolute; left: 381px; top: 610px; margin: 0;
    font-family: "Gochi Hand", cursive; font-size: 21px; line-height: 27px; color: var(--ink);
  }
</style>
</head>
<body>
  <div class="tray">
    <aside class="spine spine--left">
      <span class="spine__artist">VELMORA</span>
      <span class="spine__title">Velvet After Dark</span>
      <span class="spine__artist">VELMORA</span>
    </aside>

    <section class="panel">
      <div class="panel__wall" role="img" aria-label="Pale grey plaster wall texture"></div>
      <h1 class="album-title"><span>VELVET</span><span>AFTER</span><span>DARK</span></h1>
      <div class="artist-stamp">VELMORA</div>

      <ol class="tracklist">
        <li class="track" style="left:346px;top:70px">1. Silk Skin <span class="track__feat">(Feat. Marlon Quickstep)</span></li>
        <li class="track" style="left:355px;top:110px">2. Midnight Heat <span class="track__feat">(Feat. Dolo Vey)</span></li>
        <li class="track" style="left:367px;top:151px">3. Feel The Wave <span class="track__feat">(Feat. Tumo)</span></li>
        <li class="track" style="left:389px;top:191px">4. Hold Me Closer</li>
        <li class="track" style="left:429px;top:232px">5. Sidewayz</li>
        <li class="track" style="left:419px;top:274px">6. For Us <span class="track__feat">(Feat. Dolo Vey)</span></li>
        <li class="track" style="left:357px;top:315px">7. She Fits Right In Here</li>
        <li class="track" style="left:388px;top:356px">8. Stay Late</li>
        <li class="track" style="left:377px;top:397px">9. Weekend Is Ours</li>
        <li class="track" style="left:367px;top:438px">10. Down This Hall</li>
        <li class="track" style="left:346px;top:480px">11. We Might</li>
        <li class="track" style="left:377px;top:521px">12. Seasons Of Desire</li>
      </ol>

      <p class="credits">Copyright Information / Copyright info<br>Recorded at Information / Thank You</p>
    </section>

    <aside class="spine spine--right">
      <span class="spine__artist">VELMORA</span>
      <span class="spine__title">Velvet After Dark</span>
      <span class="spine__artist">VELMORA</span>
    </aside>
  </div>
</body>
</html>
```